Consulting, Investors, Joint Venture Website

Founded in April 2018, Marendo Consultants Limited (MCL) is an advisory consulting firm specializing in engaging investors in business ventures in Tanzania.
With extensive experience in construction, energy, oil and gas and the legal professions, our team assembles our expertise that allows foreign investors to set foot and flourish in the Tanzanian market.
MCL is locally owned, founded and registered. Our shareholders are cultured Tanzanian citizens with extensive corporate experience in South Africa, Tanzania, United Kingdom and the United States.

Our mission is to provide responsive and unrivalled professional advice from learned and experienced professionals versed in the local market, with an understanding of the cultural and logistical challenges faced by foreign investors.

Our vision is to provide a complete investor’s package that initiates with company registration, compliance and documentation services and ultimately operational facilitation services.

Target Market(s)

Foreign Investors, International companies

Industry/Entity Type

Business Consultant

Number of Pages Required

5+ page

Requirements
Must have
• It will be 5 pages - Home, About Us, Services, Portfolio, Contact Us
Nice to have
• if it can look like https://www.plorvex.example/
• or https://www.dunetri.example or http://www.quillbrook.example/

```html
<!DOCTYPE html>
<html lang="en">
<head>
<meta charset="utf-8">
<title>Marendo Consultants</title>
<link rel="stylesheet" href="https://fonts.googleapis.com/css2?family=Montserrat:wght@400;500;600;700&family=Orbitron:wght@800;900&display=swap">
<style>
:root{
  --blue:#0c56a6;
  --blue-dark:#0a4890;
  --blue-deep:#083a78;
  --orange:#f28a1a;
  --ink:#222;
  --muted:#555;
  --white:#fff;
  --footer:#232323;
  --line:#d6d6d6;
}
*{margin:0;padding:0;box-sizing:border-box}
html,body{width:1200px;height:2356px;overflow:hidden}
body{position:relative;background:var(--white);font-family:"Montserrat",Arial,sans-serif;color:var(--ink)}
.abs{position:absolute}

/* header */
.site-header{left:0;top:0;width:1200px;height:85px;background:var(--white)}
.brand{left:141px;top:22px;display:flex;align-items:center;gap:10px}
.brand-mark{width:42px;height:42px;border-radius:50%;background:var(--blue)}
.brand-name{font-family:"Montserrat",Arial,sans-serif;font-weight:700;font-size:30px;letter-spacing:2px;color:var(--blue)}
.contact-strip{top:13px;left:798px;display:flex;gap:22px;font-size:13px;color:#333;align-items:center}
.contact-strip span{display:flex;align-items:center;gap:7px}
.main-nav{left:440px;top:41px;width:760px;height:34px;background:var(--blue);border-radius:17px 0 0 17px;display:flex;align-items:center}
.main-nav a{position:absolute;color:var(--white);font-size:13px;font-weight:600;text-decoration:none;transform:translateX(-50%);top:10px;white-space:nowrap}
.main-nav a.active{color:var(--orange)}
.main-nav a.active::after{content:"";position:absolute;left:0;right:0;bottom:-12px;height:3px;background:var(--orange)}
.nav-sep{position:absolute;top:9px;width:1px;height:16px;background:rgba(255,255,255,.3)}

/* hero */
.hero{left:0;top:85px;width:1200px;height:458px;background:linear-gradient(180deg,#dedede 0%,#f4f4f4 45%,#e9e9e9 100%)}
.hero-caption{left:0;top:290px;width:537px;height:126px;background:var(--blue);border-radius:0 63px 63px 0;color:var(--white);font-size:23px;font-weight:600;line-height:33px;text-align:right;padding:14px 52px 0 0}

/* sections */
.section-title{left:0;width:1200px;text-align:center;font-family:"Orbitron",Arial,sans-serif;font-weight:900;font-size:30px;letter-spacing:3px;color:var(--blue)}
.divider{left:466px;width:268px;height:12px}
.divider::before,.divider::after{content:"";position:absolute;top:6px;width:120px;height:1px;background:var(--line)}
.divider::before{left:0}.divider::after{right:0}
.divider i{position:absolute;left:127px;top:0;width:14px;height:12px;background:#9a9a9a}
.on-blue .divider::before,.on-blue .divider::after{background:rgba(255,255,255,.35)}
.on-blue .divider i{background:rgba(255,255,255,.7)}

.welcome-text{left:151px;top:681px;width:898px;text-align:center;font-size:12.3px;line-height:23px;color:#333}
.btn-read{left:540px;top:820px;width:120px;height:35px;border-radius:18px;background:var(--blue);color:var(--white);font-size:12px;font-weight:600;text-align:center;line-height:35px}

.services{left:0;top:916px;width:1200px;height:479px;background:linear-gradient(120deg,#0a4a94 0%,#1763b4 45%,#0b4c98 100%)}
.service{width:306px;text-align:center;color:var(--white)}
.service-icon{width:132px;height:132px;margin:0 auto;border-radius:50%;background:var(--white);border:4px solid var(--orange);display:flex;align-items:center;justify-content:center}
.service h3{margin-top:20px;font-size:19px;font-weight:500;line-height:24px}
.service p{margin-top:15px;font-size:11.5px;font-weight:500;line-height:21px;padding:0 6px}

.portfolio-grid{left:141px;top:1547px;width:918px;height:446px;display:grid;grid-template-columns:repeat(3,306px);grid-template-rows:repeat(2,223px)}
.tile{position:relative}
.tile-solar{background:linear-gradient(180deg,#9fc2e6 0%,#dbe8f5 40%,#6e8f3a 70%,#4d6a22 100%)}
.tile-overlay{background:linear-gradient(160deg,#3a3a3a,#1d1d1d);color:var(--white);text-align:center}
.tile-refinery{background:linear-gradient(180deg,#e8b66a 0%,#d9a46a 35%,#7d8890 70%,#5d6870 100%)}
.tile-desk{background:linear-gradient(160deg,#c58a3e 0%,#e2b374 50%,#b07a38 100%)}
.tile-plant{background:linear-gradient(180deg,#4f7fb3 0%,#c9a57a 55%,#3d3f47 100%)}
.tile-meeting{background:linear-gradient(160deg,#e5e9ee 0%,#b9c4d1 50%,#4b5c77 100%)}
.tile-overlay .mark{width:22px;height:20px;margin:56px auto 0;background:rgba(255,255,255,.8)}
.tile-overlay p{margin-top:10px;font-size:11.5px;line-height:21px}
.tile-overlay .plus{margin:14px auto 0;width:30px;height:30px}

/* footer */
.site-footer{left:0;top:2053px;width:1200px;height:267px;background:var(--footer);color:var(--white)}
.footer-col h4{font-size:14.5px;font-weight:500;padding-bottom:8px;border-bottom:1px solid #555;width:104px}
.footer-links{list-style:none;margin-top:12px;font-size:11.5px;line-height:25.5px}
.footer-links li::before{content:"•";margin-right:8px}
.footer-links li.current{color:#2f84d6}
.vsep{top:52px;width:1px;height:165px;background:#444}
.contact-detail{margin-top:14px;font-size:11px;line-height:16px}
.contact-detail strong{display:block;font-weight:700}
.contact-line{display:flex;align-items:center;gap:10px;margin-top:8px;font-size:11px}
.field{width:183px;height:25px;background:var(--white);margin-top:8px;color:#333;font-size:10.5px;padding:5px 8px}
.field.tall{height:37px}
.btn-submit{width:85px;height:28px;background:var(--blue);margin-top:8px;font-size:12px;font-weight:600;text-align:center;line-height:28px}
.footer-brand{left:856px;top:2160px;display:flex;align-items:center;gap:8px}
.footer-brand .brand-mark{width:36px;height:36px;background:#9a9a9a}
.footer-brand .brand-name{color:#cfcfcf;font-size:26px}
.socials{left:898px;top:2201px;display:flex;gap:8px}
.socials span{width:22px;height:22px;border-radius:50%;background:#2f84d6}
.copyright{left:0;top:2320px;width:1200px;height:36px;background:var(--blue);color:var(--white);font-size:11px;font-weight:600;text-align:center;line-height:36px}
</style>
</head>
<body>

<header class="abs site-header">
  <div class="abs brand"><span class="brand-mark"></span><span class="brand-name">MARENDO</span></div>
  <div class="abs contact-strip">
    <span><svg width="13" height="13" viewBox="0 0 24 24"><path fill="#0c56a6" d="M6.6 10.8a15 15 0 0 0 6.6 6.6l2.2-2.2c.3-.3.7-.4 1-.2 1.1.4 2.3.6 3.6.6.6 0 1 .4 1 1V20c0 .6-.4 1-1 1A17 17 0 0 1 3 4c0-.6.4-1 1-1h3.5c.6 0 1 .4 1 1 0 1.3.2 2.5.6 3.6.1.3 0 .7-.2 1z"/></svg>123-456-7890</span>
    <span><svg width="14" height="11" viewBox="0 0 24 18"><rect width="24" height="18" rx="2" fill="#0c56a6"/><path d="M2 3l10 7 10-7" stroke="#fff" stroke-width="2" fill="none"/></svg>info@mclconsulting.example</span>
  </div>
  <nav class="abs main-nav">
    <a class="active" href="#" style="left:53px">HOME</a>
    <span class="nav-sep" style="left:110px"></span>
    <a href="#" style="left:172px">ABOUT US</a>
    <span class="nav-sep" style="left:240px"></span>
    <a href="#" style="left:301px">SERVICES</a>
    <span class="nav-sep" style="left:367px"></span>
    <a href="#" style="left:433px">PORTFOLIO</a>
    <span class="nav-sep" style="left:505px"></span>
    <a href="#" style="left:575px">CONTACT US</a>
  </nav>
</header>

<section class="abs hero" role="img" aria-label="Photo of a red chess king standing ahead of a row of white pawns"></section>
<div class="abs hero-caption">We are an new advisory consulting firm<br>specializing in engaging investors in<br>business ventures in Tanzania.</div>

<h2 class="abs section-title" style="top:594px">WELCOME TO MARENDO</h2>
<div class="abs divider" style="top:643px"><i></i></div>
<p class="abs welcome-text">Lorem ipsum dolor sit amet, consectetuer adipiscing elit, sed diam nonummy nibh euismod tincidunt ut laoreet dolore magna aliquam erat volutpat. Ut wisi enim ad minim veniam, quis nostrud exerci tation ullamcorper suscipit lobortis nisl ut aliquip ex ea commodo consequat. Duis autem vel eum iriure dolor in hendrerit in vulputate velit esse molestie consequat, vel illum dolore eu feugiat nulla facilisis at vero eros et accumsan et iusto odio dignissim qui blandit praesent luptatum zzril delenit augue duis dolore te feugait nulla facilisi. Lorem ipsum dolor sit amet, consectetuer adipiscing elit, sed diam nonummy nibh euismod tincidunt ut laoreet dolore magna aliquam erat volutpat.</p>
<div class="abs btn-read">READ MORE</div>

<section class="abs services on-blue">
  <h2 class="abs section-title" style="top:51px;color:#fff">OUR SERVICES</h2>
  <div class="abs divider" style="top:100px"><i></i></div>
  <div class="abs service" style="left:141px;top:143px">
    <div class="service-icon"><svg width="58" height="52" viewBox="0 0 58 52" fill="none" stroke="#0c56a6" stroke-width="2"><rect x="8" y="6" width="32" height="40"/><path d="M4 10v40h32"/><path d="M14 16h20M14 22h20M14 28h20M14 34h14"/><path d="M48 6l5 0v34l-2.5 6-2.5-6z"/></svg></div>
    <h3>Compliance And<br>Documentation</h3>
    <p>Lorem ipsum dolor sit amet, consectetuer adipiscing elit, sed diam nonummy nibh euismod tincidunt ut laoreet dolore magna aliquam erat volutpat.</p>
  </div>
  <div class="abs service" style="left:449px;top:143px">
    <div class="service-icon"><svg width="58" height="58" viewBox="0 0 58 58" fill="none" stroke="#0c56a6" stroke-width="2"><circle cx="29" cy="29" r="7"/><path d="M29 14l3 0 1 4 4 2 4-2 3 3-2 4 2 4 4 1v4l-4 1-2 4 2 4-3 3-4-2-4 2-1 4h-6l-1-4-4-2-4 2-3-3 2-4-2-4-4-1v-4l4-1 2-4-2-4 3-3 4 2 4-2 1-4z"/><path d="M10 18a22 22 0 0 1 14-11M48 40a22 22 0 0 1-14 11"/></svg></div>
    <h3>Ultimately Operational<br>Facilitation</h3>
    <p>Lorem ipsum dolor sit amet, consectetuer adipiscing elit, sed diam nonummy nibh euismod tincidunt ut laoreet dolore magna aliquam erat volutpat.</p>
  </div>
  <div class="abs service" style="left:755px;top:143px">
    <div class="service-icon"><svg width="60" height="54" viewBox="0 0 60 54" fill="none" stroke="#0c56a6" stroke-width="2"><circle cx="17" cy="30" r="5"/><path d="M7 46c0-7 4-10 10-10s10 3 10 10z"/><circle cx="43" cy="30" r="5"/><path d="M33 46c0-7 4-10 10-10s10 3 10 10z"/><path d="M18 14a16 12 0 0 1 24 0M42 14l0-5M42 14l-5 0"/></svg></div>
    <h3>Business<br>Consulting</h3>
    <p>Lorem ipsum dolor sit amet, consectetuer adipiscing elit, sed diam nonummy nibh euismod tincidunt ut laoreet dolore magna aliquam erat volutpat.</p>
  </div>
</section>

<h2 class="abs section-title" style="top:1454px">OUR PORTFOLIO</h2>
<div class="abs divider" style="top:1504px"><i></i></div>
<div class="abs portfolio-grid">
  <div class="tile tile-solar" role="img" aria-label="Photo of solar panels on a green field under a blue sky"></div>
  <div class="tile tile-overlay" role="img" aria-label="Darkened project photo with hover caption">
    <div class="mark"></div>
    <p>Lorem ipsum dolor sit amet, consectetuer<br>adipiscing elit, sed diam nonummy</p>
    <svg class="plus" viewBox="0 0 30 30" fill="none" stroke="#fff" stroke-width="1.5"><circle cx="15" cy="15" r="13"/><path d="M15 8v14M8 15h14"/></svg>
  </div>
  <div class="tile tile-refinery" role="img" aria-label="Photo of an oil storage terminal at sunset"></div>
  <div class="tile tile-desk" role="img" aria-label="Photo of a desk with laptops and printed charts seen from above"></div>
  <div class="tile tile-plant" role="img" aria-label="Photo of a power plant with chimneys at dusk"></div>
  <div class="tile tile-meeting" role="img" aria-label="Photo of colleagues reviewing documents at an office table"></div>
</div>

<footer class="abs site-footer">
  <div class="abs footer-col" style="left:143px;top:45px">
    <h4>Quick Links</h4>
    <ul class="footer-links">
      <li class="current">Home</li><li>About Us</li><li>Services</li><li>Portfolio</li><li>Contact Us</li>
    </ul>
  </div>
  <span class="abs vsep" style="left:292px"></span>
  <div class="abs footer-col" style="left:338px;top:45px">
    <h4>Contact Detail</h4>
    <div class="contact-detail"><strong>MARENDO CONSULTANTS</strong>Lorem ipsum dolor sit et,<br>conse cingrer eed diam</div>
    <div class="contact-line" style="margin-top:14px"><svg width="11" height="11" viewBox="0 0 24 24"><path fill="#fff" d="M6.6 10.8a15 15 0 0 0 6.6 6.6l2.2-2.2c.3-.3.7-.4 1-.2 1.1.4 2.3.6 3.6.6.6 0 1 .4 1 1V20c0 .6-.4 1-1 1A17 17 0 0 1 3 4c0-.6.4-1 1-1h3.5c.6 0 1 .4 1 1 0 1.3.2 2.5.6 3.6.1.3 0 .7-.2 1z"/></svg>+012 345 6789</div>
    <div class="contact-line"><svg width="12" height="11" viewBox="0 0 24 22"><rect x="5" y="0" width="14" height="6" fill="#fff"/><rect x="0" y="7" width="24" height="9" rx="2" fill="#fff"/><rect x="5" y="14" width="14" height="8" fill="#fff" stroke="#232323" stroke-width="2"/></svg>+012 345 6789</div>
    <div class="contact-line"><svg width="12" height="9" viewBox="0 0 24 18"><rect width="24" height="18" rx="2" fill="#fff"/><path d="M2 3l10 7 10-7" stroke="#232323" stroke-width="2" fill="none"/></svg>info@mclconsulting.example</div>
  </div>
  <span class="abs vsep" style="left:532px"></span>
  <div class="abs footer-col" style="left:580px;top:45px">
    <h4 style="width:183px">Quick Inquiry</h4>
    <div class="field" style="margin-top:10px">Name</div>
    <div class="field">Email</div>
    <div class="field tall">Message</div>
    <div class="btn-submit">Submit</div>
  </div>
  <span class="abs vsep" style="left:807px"></span>
</footer>
<div class="abs footer-brand"><span class="brand-mark"></span><span class="brand-name">MARENDO</span></div>
<div class="abs socials" aria-label="Social links"><span></span><span></span><span></span><span></span></div>
<div class="abs copyright">Copyright 2018 Marendo Consultants. All Rights Reserved.</div>

</body>
</html>
```